Brightstep Dance Business Card

I'm looking for a two-sided business card design to promote my country dance busness. Cowboy hats, boots, and wood grain floor textures, are all appropriate to use.
On one side I want it to say:
Brightstep Dance
with
Mark
Take The Challenge - Experience The Growth
210-555-0143
On the other side I want:
A place for a Head Shot
The Quote: Experience Is The Best Teacher
A two column bullet list with the following:
First column: Two Step, Waltz, Triple Two, Polka
Second column: Cha-Cha, West Coast, East Cost, NightClub
My Name: Mark Delway
My Phone Number: 210-555-0143

```html
<!DOCTYPE html>
<html lang="en">
<head>
<meta charset="utf-8">
<title>Brightstep Dance Business Card</title>
<link href="https://fonts.googleapis.com/css2?family=Cinzel:wght@600;700&family=Poppins:wght@400;500;600&family=Syncopate:wght@700&family=Yellowtail&display=swap" rel="stylesheet">
<style>
  :root {
    --backdrop: #1a1a1a;
    --cream: #f6f4e8;
    --brand-red: #931214;
    --olive: #4a4a1a;
    --ink: #141414;
    --white: #ffffff;
    --photo-light: #c9cace;
    --photo-dark: #8f8f92;
  }
  * { margin: 0; padding: 0; box-sizing: border-box; }
  html, body { width: 1093px; height: 1200px; overflow: hidden; background: var(--backdrop); }
  .canvas { position: relative; width: 1093px; height: 1200px; }

  .card { position: absolute; left: 264px; width: 580px; height: 357px; }
  .card-front { top: 226px; background: var(--cream); }
  .card-back { top: 620px; background: var(--brand-red); }

  .studio-name {
    position: absolute; top: 28px; left: 0; right: 0; text-align: center;
    font-family: "Cinzel", serif; font-weight: 700; font-size: 40px;
    color: var(--olive); letter-spacing: 0.5px;
  }
  .with {
    position: absolute; top: 80px; left: 0; right: 0; text-align: center;
    font-family: "Poppins", sans-serif; font-weight: 500; font-size: 19px;
    letter-spacing: 2px; color: var(--ink);
  }
  .teacher-first {
    position: absolute; top: 86px; left: 0; right: 0; text-align: center;
    font-family: "Yellowtail", cursive; font-size: 92px; line-height: 1;
    color: var(--brand-red);
  }
  .tagline-band {
    position: absolute; top: 215px; left: 0; right: 0; height: 60px;
    background: var(--brand-red); display: flex; align-items: center; justify-content: center;
  }
  .tagline {
    font-family: "Poppins", sans-serif; font-weight: 500; font-size: 20px;
    letter-spacing: 1px; color: var(--white); text-transform: uppercase;
  }
  .phone {
    position: absolute; left: 0; right: 0; text-align: center;
    font-family: "Syncopate", sans-serif; font-weight: 700; letter-spacing: 1px;
  }
  .card-front .phone { top: 293px; font-size: 29px; color: var(--brand-red); }

  .headshot {
    position: absolute; left: 30px; top: 38px; width: 192px; height: 229px;
    border: 2px solid var(--white);
    background: radial-gradient(ellipse at 50% 40%, var(--photo-light), var(--photo-dark));
  }
  .headshot-label {
    position: absolute; bottom: 14px; left: 0; right: 0; text-align: center;
    font-family: "Poppins", sans-serif; font-size: 18px; color: #333;
  }
  .name-tag {
    position: absolute; left: 30px; top: 281px; width: 192px; height: 39px;
    background: var(--cream); display: flex; align-items: center; justify-content: center;
    font-family: "Poppins", sans-serif; font-weight: 600; font-size: 26px; color: var(--brand-red);
  }
  .name-tag::before {
    content: ""; position: absolute; top: -7px; left: 8px;
    border-left: 5px solid transparent; border-right: 5px solid transparent;
    border-bottom: 7px solid var(--cream);
  }
  .quote {
    position: absolute; left: 250px; width: 290px; top: 36px; text-align: center;
    font-family: "Cinzel", serif; font-weight: 700; font-size: 29px; line-height: 35px;
    color: var(--white);
  }
  .styles-list {
    position: absolute; top: 128px; list-style: none;
    font-family: "Poppins", sans-serif; font-size: 21px; line-height: 26px; color: var(--white);
  }
  .styles-list li { padding-left: 18px; position: relative; }
  .styles-list li::before {
    content: ""; position: absolute; left: 0; top: 10px; width: 8px; height: 8px;
    border-radius: 50%; background: var(--white);
  }
  .styles-list.col-one { left: 260px; }
  .styles-list.col-two { left: 413px; }
  .divider {
    position: absolute; left: 322px; top: 265px; width: 177px; height: 2px;
    background: rgba(255,255,255,0.35);
  }
  .card-back .phone { top: 285px; left: 250px; right: 28px; font-size: 25px; color: var(--white); }
</style>
</head>
<body>
<div class="canvas">
  <section class="card card-front">
    <h1 class="studio-name">Brightstep Dance</h1>
    <p class="with">WITH</p>
    <p class="teacher-first">Mark</p>
    <div class="tagline-band"><p class="tagline">Take the Challenge - Experience the Growth</p></div>
    <p class="phone">210-555-0143</p>
  </section>

  <section class="card card-back">
    <div class="headshot" role="img" aria-label="Head shot of Mark Delway">
      <span class="headshot-label">PHOTO HERE</span>
    </div>
    <div class="name-tag">Mark Delway</div>
    <h2 class="quote">Experience Is The Best Teacher</h2>
    <ul class="styles-list col-one">
      <li>Two Step</li><li>Waltz</li><li>Triple Two</li><li>Polka</li>
    </ul>
    <ul class="styles-list col-two">
      <li>Cha-Cha</li><li>West Coast</li><li>East Cost</li><li>NightClub</li>
    </ul>
    <div class="divider"></div>
    <p class="phone">210-555-0143</p>
  </section>
</div>
</body>
</html>
```